Kestrel Valley Alpine Riders Society needs a business card design

We need a business card design for our newly incorporated KVARS. We are helping the NZ Chinese community, as well as everyone else, to organise ski & snowboarding trips, training, and equipments. The design should be creative, energetic, young and vibrant.

Industry/Entity Type

Social Club

Contact Information for Business Card

Logo; Kestrel Valley Alpine Riders Society; Name: Oliver Brandt; Position: President; Address: 42 Marwick Rd, Epsom, Auckland 1051; Mobile: 020 7826 1957; Email: oliver@kvars-club.example; Web: www.kvars-club.example

Requirements
Must have
• 1, The text "Kestrel Valley Alpine Riders Society" should be put together with the supplied logo file to form a new complete logo combination.
• 2, Final design files should be in Adobe Illustrator format and all text must be editable.
Nice to have
• two or three colours

```html
<!DOCTYPE html>
<html lang="en">
<head>
<meta charset="utf-8">
<title>KVARS Business Card</title>
<link rel="stylesheet" href="https://fonts.googleapis.com/css2?family=Open+Sans:wght@400;600;700;800&display=swap">
<style>
  :root {
    --backdrop: #3a3a3b;
    --card: #1e1e1f;
    --blue: #2aa7e1;
    --blue-deep: #2a6fc2;
    --ink-light: #f2f2f2;
    --emboss: #8a8a8c;
  }
  * { box-sizing: border-box; margin: 0; padding: 0; }
  html, body {
    width: 1200px; height: 1000px; overflow: hidden;
    background: var(--backdrop);
    font-family: "Open Sans", Arial, sans-serif;
  }
  .canvas {
    width: 1200px; height: 1000px;
    display: flex; flex-direction: column; align-items: center; justify-content: center;
    gap: 40px;
  }
  .card {
    width: 770px; height: 440px;
    background: var(--card);
    border-radius: 3px;
    box-shadow: 0 18px 40px rgba(0,0,0,0.45);
    position: relative;
  }
  .card-front { display: flex; align-items: center; justify-content: center; }
  .wordmark {
    font-weight: 800;
    letter-spacing: 1px;
    line-height: 1;
  }
  .card-front .wordmark { font-size: 78px; color: var(--emboss); }
  .card-back { display: flex; align-items: center; padding-left: 60px; }
  .card-back .wordmark { font-size: 84px; color: var(--blue); width: 300px; }
  .details { margin-left: 50px; }
  .identity {
    border-left: 3px solid var(--blue-deep);
    padding: 4px 0 4px 22px;
    margin-bottom: 26px;
  }
  .person-name { color: var(--blue); font-size: 30px; font-weight: 700; letter-spacing: 1px; }
  .person-role { color: var(--ink-light); font-size: 20px; font-weight: 700; letter-spacing: 0.5px; margin-top: 2px; }
  .contact {
    border-left: 3px solid var(--blue);
    padding: 4px 0 4px 22px;
    color: var(--ink-light);
    font-size: 19px;
    line-height: 1.35;
  }
  .address { margin-bottom: 14px; }
  .contact-row { display: flex; align-items: center; gap: 12px; }
  .contact-row svg { width: 18px; height: 18px; flex: none; fill: var(--blue); }
  .accent { color: var(--blue); }
</style>
</head>
<body>
  <main class="canvas">
    <section class="card card-front" aria-label="Card front">
      <div class="wordmark">KVARS</div>
    </section>

    <section class="card card-back" aria-label="Card back">
      <div class="wordmark">KVARS</div>
      <div class="details">
        <div class="identity">
          <p class="person-name">Oliver Brandt</p>
          <p class="person-role">President</p>
        </div>
        <div class="contact">
          <p class="address">42 Marwick Rd, Epsom,<br>Auckland 1051</p>
          <p class="contact-row">
            <svg viewBox="0 0 24 24" aria-hidden="true"><path d="M6.6 10.8c1.4 2.8 3.8 5.1 6.6 6.6l2.2-2.2c.3-.3.7-.4 1-.2 1.1.4 2.3.6 3.6.6.6 0 1 .4 1 1V20c0 .6-.4 1-1 1C10.6 21 3 13.4 3 4c0-.6.4-1 1-1h3.5c.6 0 1 .4 1 1 0 1.3.2 2.5.6 3.6.1.3 0 .7-.2 1z"/></svg>
            <span>020 7826 1957</span>
          </p>
          <p class="contact-row">
            <svg viewBox="0 0 24 24" aria-hidden="true"><path d="M2 5h20v2l-10 6L2 7z"/><path d="M2 9l10 6 10-6v10H2z"/></svg>
            <span>oliver@kvars-club.example</span>
          </p>
          <p class="contact-row">
            <svg viewBox="0 0 24 24" aria-hidden="true"><path d="M10 2a8 8 0 0 1 6.3 12.9l5.4 5.4-1.4 1.4-5.4-5.4A8 8 0 1 1 10 2zm0 3a5 5 0 1 0 0 10 5 5 0 0 0 0-10z"/></svg>
            <span>www.<span class="accent">kvars-club</span>.example</span>
          </p>
        </div>
      </div>
    </section>
  </main>
</body>
</html>
```